Velorin Pain Management (this is the name of our clinics)

We are a medical group who will open a few new offices to see patients who are interested in medical cannabis therapy. We want to express this in a poster or a life size stand-alone cardboard ad to inform patients that 'this is the place'. We may also want to use the electronic ad on an e-billboard. We will not dispense any of the cannabis on sit but we will see patients and issue prescriptions and user cards, and we will align those patients with a federal grower who will deliver the meds (cannabis oil) to their place. We dont have a logo yet, so we want that as well.

Target Market(s)

Patients with repetitive strain injuries and other chronic pains, or post traumatic stress disorder from the military of victims of traumatic accidents or assaults.

Industry/Entity Type

Medical And Science

Requirements
Must have
• A poster showing a patient in clinic setting with our clinic name (Velorin Pain Management)

```html
<!DOCTYPE html>
<html lang="en">
<head>
<meta charset="utf-8">
<title>Velorin Pain Management – Poster</title>
<link rel="stylesheet" href="https://fonts.googleapis.com/css2?family=Oswald:wght@400;500&display=swap">
<style>
  :root {
    --page-bg: #ffffff;
    --green-light: #3fb04e;
    --green-mid: #34a046;
    --green-deep: #24823a;
    --ink-white: #ffffff;
    --rule: rgba(255, 255, 255, 0.75);
  }
  * { margin: 0; padding: 0; box-sizing: border-box; }
  html, body {
    width: 1200px;
    height: 900px;
    overflow: hidden;
    background: var(--page-bg);
  }
  .canvas {
    position: relative;
    width: 1200px;
    height: 900px;
  }
  .poster {
    position: absolute;
    left: 380px;
    top: 118px;
    width: 440px;
    height: 664px;
    overflow: hidden;
    color: var(--ink-white);
    font-family: "Oswald", "Arial Narrow", sans-serif;
  }
  .poster__photo {
    position: absolute;
    inset: 0;
    background:
      radial-gradient(ellipse 45% 35% at 90% 25%, rgba(30, 110, 48, 0.55), transparent 70%),
      radial-gradient(ellipse 50% 40% at 80% 70%, rgba(28, 105, 45, 0.6), transparent 70%),
      radial-gradient(ellipse 40% 30% at 15% 15%, rgba(80, 190, 95, 0.35), transparent 70%),
      linear-gradient(100deg, var(--green-light) 0%, var(--green-mid) 55%, var(--green-deep) 100%);
  }
  .brand-mark {
    position: absolute;
    left: 50%;
    top: 52px;
    width: 204px;
    height: 204px;
    margin-left: -102px;
    border-radius: 50%;
    background: var(--ink-white);
  }
  .brand-name {
    position: absolute;
    left: 0;
    right: 0;
    top: 262px;
    text-align: center;
    font-weight: 500;
    font-size: 130px;
    line-height: 1;
    letter-spacing: -0.005em;
  }
  .brand-descriptor {
    position: absolute;
    left: 0;
    right: 0;
    top: 405px;
    text-align: center;
    font-weight: 500;
    font-size: 26px;
    line-height: 1;
    letter-spacing: 0.44em;
    padding-left: 0.44em;
  }
  .tagline {
    position: absolute;
    left: 38px;
    right: 38px;
    top: 514px;
    text-align: center;
    font-weight: 400;
    font-size: 20px;
    line-height: 1;
    letter-spacing: 0.02em;
  }
  .tagline__question {
    padding-bottom: 10px;
    border-bottom: 1px solid var(--rule);
  }
  .tagline__answer {
    padding-top: 10px;
  }
</style>
</head>
<body>
  <main class="canvas">
    <section class="poster">
      <div class="poster__photo" role="img" aria-label="Soft-focus photograph of a patient in a clinic setting, tinted green"></div>
      <div class="brand-mark" aria-hidden="true"></div>
      <h1 class="brand-name">Velorin</h1>
      <p class="brand-descriptor">PAIN MANAGEMENT</p>
      <div class="tagline">
        <p class="tagline__question">Interested in Medical Cannabis therapy?</p>
        <p class="tagline__answer">You have questions. We have answers.</p>
      </div>
    </section>
  </main>
</body>
</html>
```